Thornfield Marsh, LLC Website

We are a small law firm in need of a website that contains the following:
1. Attractive main page
2. About us/attorney info for three people: Leonard Thornfield (attorney), Brent Marsh (attorney), and Melinda Carrow (legal assistant). We have bio's ready to submit.
3. Blog/video page. We'd like to post blogs and videos to help drive traffic
4. Multidistrict Litigation and Class Actions page, where we post information regarding active MDLs and Class actions that we are doing intake on.
Updates

Can you also please use the color "gold" in the design and logo? Thanks.

Industry/Entity Type

Legal

Coding

Coded - Design and coding required

Number of Pages Required

1 page

Colors
0054AA
0677BA
7BADD7
CADEEF
E8F1F8

Requirements
Must have
• 1. Attractive main page 2. About us/attorney info for three people: Leonard Thornfield (attorney), Brent Marsh (attorney), and Melinda Carrow (legal assistant). We have bio's ready to submit. 3. Blog/video page. We'd like to post blogs and videos to help drive traffic 4. Multidistrict Litigation and Class Actions page, where we post information regarding active MDLs and Class actions that we are doing intake on.

```html
<!DOCTYPE html>
<html lang="en">
<head>
<meta charset="utf-8">
<title>Thornfield Marsh, LLC — Lawyers</title>
<link href="https://fonts.googleapis.com/css2?family=Montserrat:wght@500;600;700;800&family=Poppins:wght@400;500;600&display=swap" rel="stylesheet">
<style>
:root{
  --navy:#0a1f8f;
  --navy-dark:#061566;
  --blue:#1ea5f3;
  --ink:#1d1d2b;
  --muted:#444;
  --grey-bg:#f4f4f5;
  --white:#ffffff;
  --gold:#c9a646;
  --gold-light:#e2c677;
}
*{box-sizing:border-box;margin:0;padding:0}
html,body{width:1200px;height:4107px;overflow:hidden}
body{position:relative;font-family:"Poppins",sans-serif;color:var(--ink);background:var(--white)}
.abs{position:absolute}
h1,h2,h3,.brand,.btn{font-family:"Montserrat",sans-serif}

/* header */
.site-header{left:0;top:0;width:1200px;height:113px;background:var(--white);border-bottom:3px solid var(--gold)}
.brand{display:flex;align-items:center;gap:12px;font-weight:700;color:var(--navy);font-size:24px;white-space:nowrap}
.brand .mark{width:40px;height:40px;background:var(--gold)}
.site-header .brand{left:70px;top:35px}
.nav{left:640px;top:44px;display:flex;gap:36px;font-size:13px;font-weight:500;letter-spacing:.3px}
.nav a{color:var(--ink);text-decoration:none}
.nav a.active{color:var(--blue);border-bottom:2px solid var(--gold);padding-bottom:3px}
.pill{border-radius:40px;display:flex;align-items:center;justify-content:center;text-decoration:none}
.header-cta{left:1001px;top:38px;width:137px;height:34px;background:var(--blue);color:var(--white);font-size:14px;font-weight:500}

/* hero */
.hero{left:0;top:113px;width:1200px;height:652px;background:linear-gradient(90deg,#5b4634 0%,#3b3028 28%,#1b1d2c 48%,#0b1022 62%,#090e1f 100%)}
.hero-photo{left:0;top:0;width:560px;height:652px;background:radial-gradient(ellipse at 40% 40%,#c9a48a 0%,#7b5c46 35%,#3c2e26 70%,rgba(30,25,30,0) 100%)}
.hero .eyebrow{left:617px;top:120px;color:var(--gold-light);font-size:24px}
.hero h1{left:615px;top:165px;color:var(--white);font-weight:800;font-size:66px;line-height:84px;letter-spacing:0;white-space:nowrap}
.hero h1 small{font-size:40px;font-weight:700;color:var(--gold)}
.hero .lead{left:622px;top:355px;width:480px;color:var(--white);font-size:16px;line-height:27px}
.hero-cta{left:618px;top:430px;width:256px;height:63px;background:var(--white);color:var(--navy);font-size:22px;font-weight:600;gap:18px;padding-left:14px}
.arrow-dot{width:48px;height:48px;border-radius:50%;background:var(--blue);display:flex;align-items:center;justify-content:center}

/* section headings */
.section-title{left:0;width:1200px;text-align:center}
.section-title h2{color:var(--navy);font-size:40px;font-weight:700;line-height:44px}
.section-title .kicker{display:inline-flex;align-items:center;gap:6px;color:var(--blue);font-size:12px;font-weight:600;margin-top:2px}
.section-title .kicker::before,.section-title .kicker::after{content:"";width:50px;height:2px;background:var(--gold)}

/* services */
.services{left:0;top:765px;width:1200px;height:786px;background:var(--grey-bg)}
.service-card{top:164px;width:331px;height:436px;background:var(--white);box-shadow:0 2px 8px rgba(0,0,0,.12);text-align:center;border-bottom:3px solid var(--gold)}
.service-card .photo{position:absolute;left:17px;top:18px;width:297px;height:213px;border-radius:4px}
.service-card h3{position:absolute;left:0;top:248px;width:100%;color:var(--navy);font-size:22px;font-weight:600}
.service-card p{position:absolute;left:20px;top:290px;width:291px;font-size:14px;line-height:25.5px;color:var(--muted)}
.small-btn{position:absolute;left:116px;top:378px;width:110px;height:32px;background:var(--blue);color:var(--white);font-size:13px;border-radius:8px;display:flex;align-items:center;justify-content:center}
.view-more{left:505px;top:663px;width:177px;height:50px;background:var(--navy);color:var(--white);font-size:16px;font-weight:500;gap:14px;padding-left:14px;box-shadow:0 0 0 3px var(--gold-light)}
.view-more .arrow-dot{width:36px;height:36px}

/* about */
.about{left:0;top:1551px;width:1200px;height:747px;background:var(--white)}
.member-photo{top:188px;width:322px;height:435px;border-radius:3px}
.member-card{top:566px;text-align:center;border-radius:6px 6px 0 0}
.member-card h3{font-size:18px;font-weight:600;margin-top:14px;white-space:nowrap}
.member-card .role{font-size:11px;margin-top:1px}
.member-card .icons{display:flex;gap:9px;justify-content:center;margin-top:8px}
.member-card .icons span{width:17px;height:17px;border-radius:3px}
.member-card.featured{background:var(--navy);color:var(--white);height:110px;border-top:3px solid var(--gold)}
.member-card.featured .role{color:var(--gold-light)}
.member-card.featured .icons span{background:var(--blue)}
.member-card.plain{background:var(--white);color:var(--ink);height:99px}
.member-card.plain .icons span{background:#9a9a9a}

/* passion band */
.passion{left:0;top:2298px;width:1200px;height:452px;background:linear-gradient(180deg,#0b2196 0%,#0a1c86 100%);text-align:center}
.passion h2{position:absolute;left:0;top:85px;width:100%;color:var(--blue);font-size:62px;font-weight:700;line-height:67px;letter-spacing:-.5px}
.passion h2 .gold{color:var(--gold)}
.passion p{position:absolute;left:180px;top:243px;width:840px;color:var(--white);font-size:14px;line-height:18px;font-weight:500}
.band-btn{top:318px;height:48px;font-size:16px;color:var(--white)}
.band-btn.solid{left:324px;width:261px;background:var(--blue)}
.band-btn.ghost{left:609px;width:199px;border:1.5px solid var(--gold)}

/* news */
.news{left:0;top:2750px;width:1200px;height:908px;background:#f7f7f8}
.news-card{top:199px;width:365px;height:602px;background:var(--white);box-shadow:0 2px 8px rgba(0,0,0,.12)}
.news-card .photo{position:absolute;left:10px;top:11px;width:345px;height:233px;border-radius:6px}
.news-card .date{position:absolute;left:27px;top:271px;color:var(--gold);font-size:13px;display:flex;gap:5px;align-items:center}
.news-card h3{position:absolute;left:27px;top:295px;width:315px;font-family:"Poppins",sans-serif;font-size:19px;font-weight:500;line-height:28px}
.news-card h3.hover{color:var(--navy);text-decoration:underline}
.news-card p{position:absolute;left:27px;top:360px;width:300px;font-size:12px;line-height:22.7px;color:var(--muted);text-align:justify}
.news-card .read{position:absolute;left:27px;top:517px;width:112px;height:38px;background:var(--navy);color:var(--white);font-size:12px}
.slider-arrow{width:36px;height:36px;border-radius:50%;display:flex;align-items:center;justify-content:center;top:485px}

/* footer */
.site-footer{left:0;top:3658px;width:1200px;height:449px;background:var(--navy);border-top:4px solid var(--gold)}
.site-footer .brand{left:159px;top:170px;color:var(--white);font-size:22px}
.site-footer .brand .mark{width:36px;height:36px}
.socials{left:207px;top:247px;display:flex;gap:10px}
.socials span{width:38px;height:38px;border-radius:50%;background:var(--white)}
.footer-col h3{color:var(--white);font-size:24px;font-weight:600}
.footer-col h3::after{content:"";display:block;width:58px;height:2px;background:var(--gold);margin-top:10px}
.links{left:536px;top:100px}
.links ul{list-style:none;margin-top:20px}
.links li{color:var(--white);font-size:15px;line-height:32.5px;display:flex;align-items:center;gap:16px;margin-left:2px}
.links li::before{content:"";width:7px;height:7px;border-radius:50%;background:var(--gold)}
.contact{left:794px;top:100px}
.contact-row{position:absolute;left:22px;display:flex;gap:16px;color:var(--white);font-size:15px;line-height:23px;white-space:nowrap}
.contact-row .ico{width:28px;height:28px;border-radius:50%;background:var(--white);display:flex;align-items:center;justify-content:center;flex:none}
.rule{left:70px;top:346px;width:1067px;height:1px;background:rgba(255,255,255,.6)}
.copyright{left:0;top:374px;width:1200px;text-align:center;color:var(--white);font-size:15px}
</style>
</head>
<body>

<header class="abs site-header">
  <div class="abs brand"><span class="mark"></span>THORNFIELD MARSH, LLC</div>
  <nav class="abs nav">
    <a class="active" href="#">HOME</a><a href="#">ABOUT US</a><a href="#">SERVICES</a><a href="#">BLOGS</a>
  </nav>
  <a class="abs pill header-cta" href="#">Contact Us</a>
</header>

<section class="abs hero">
  <div class="abs hero-photo" role="img" aria-label="Photo of a lawyer speaking at a microphone in a courtroom"></div>
  <p class="abs eyebrow">Welcome To</p>
  <h1 class="abs">THORNFIELD<br>MARSH <small>LLC</small></h1>
  <p class="abs lead">Lorem ipsum dolor sit amet, consectetur adipiscing elit, sed do eiusmod tempor incididunt ut labore et dolore</p>
  <a class="abs pill hero-cta" href="#">CONTACT US
    <span class="arrow-dot"><svg width="20" height="20" viewBox="0 0 20 20"><path d="M7 3l7 7-7 7" fill="none" stroke="#fff" stroke-width="3"/></svg></span>
  </a>
</section>

<section class="abs services">
  <div class="abs section-title" style="top:74px"><h2>OUR SERVICES</h2><span class="kicker">WHAT WE DO</span></div>

  <article class="abs service-card" style="left:69px">
    <div class="photo" role="img" aria-label="Photo of a hand signing a document" style="background:linear-gradient(135deg,#3a2518,#a8734a 55%,#e7d6c2)"></div>
    <h3>CIVIL LAW</h3>
    <p>Lorem ipsum dolor sit amet, consectetur adipiscing elit, sed do eiusmod tempor incididunt ut labore et dolore magna</p>
    <span class="small-btn">Read More</span>
  </article>
  <article class="abs service-card" style="left:426px">
    <div class="photo" role="img" aria-label="Photo of business people shaking hands at a meeting table" style="background:linear-gradient(135deg,#d9dde2,#8b9099 50%,#2d3036)"></div>
    <h3>CRIMINAL LAW</h3>
    <p>Lorem ipsum dolor sit amet, consectetur adipiscing elit, sed do eiusmod tempor incididunt ut labore et dolore magna</p>
    <span class="small-btn">Read More</span>
  </article>
  <article class="abs service-card" style="left:781px">
    <div class="photo" role="img" aria-label="Photo of a handshake over a contract and house keys" style="background:linear-gradient(135deg,#1e3a6a,#5a7aa8 45%,#c8b69a)"></div>
    <h3>ADMINISTRATIVE LAW</h3>
    <p>Lorem ipsum dolor sit amet, consectetur adipiscing elit, sed do eiusmod tempor incididunt ut labore et dolore magna</p>
    <span class="small-btn">Read More</span>
  </article>

  <a class="abs pill view-more" href="#">VIEW MORE
    <span class="arrow-dot"><svg width="16" height="16" viewBox="0 0 20 20"><path d="M7 3l7 7-7 7" fill="none" stroke="#fff" stroke-width="3"/></svg></span>
  </a>
</section>

<section class="abs about">
  <div class="abs section-title" style="top:83px"><h2>ABOUT US</h2><span class="kicker">WHO WE ARE</span></div>

  <div class="abs member-photo" style="left:100px;background:linear-gradient(180deg,#dfe6ea,#b9c3c8 55%,#1f2330 85%)" role="img" aria-label="Portrait of attorney Leonard Thornfield in an office"></div>
  <div class="abs member-photo" style="left:457px;background:linear-gradient(180deg,#e9ecee,#c8cdd1 55%,#1c1e26 85%)" role="img" aria-label="Portrait of attorney Brent Marsh in an office"></div>
  <div class="abs member-photo" style="left:810px;background:linear-gradient(180deg,#5c6f84,#9aa7b3 45%,#1b1d22 85%)" role="img" aria-label="Portrait of legal assistant Melinda Carrow outside a building"></div>

  <div class="abs member-card featured" style="left:139px;width:242px">
    <h3>LEONARD THORNFIELD</h3><p class="role">Attorney</p>
    <div class="icons"><span></span><span></span><span></span></div>
  </div>
  <div class="abs member-card plain" style="left:499px;width:239px">
    <h3>BRENT MARSH</h3><p class="role">Attorney</p>
    <div class="icons"><span></span><span></span><span></span></div>
  </div>
  <div class="abs member-card plain" style="left:851px;width:239px">
    <h3>MELINDA CARROW</h3><p class="role">Legal Assistant</p>
    <div class="icons"><span></span><span></span><span></span></div>
  </div>
</section>

<section class="abs passion">
  <h2>A LAW FIRM WITH A PASSION<br>FOR <span class="gold">BEST SUCCESS.</span></h2>
  <p>Lorem ipsum dolor sit amet, consectetur adipiscing elit, sed do eiusmod tempor incididunt ut labore et dolore magna aliqua. Quis ipsum suspendisse ultrices gravida. Risus commodo viverra maecenas accumsan lacus vel facilisis.</p>
  <a class="abs pill band-btn solid" href="#">MULTIDISTRICT LITIGATION</a>
  <a class="abs pill band-btn ghost" href="#">CLASS ACTIONS</a>
</section>

<section class="abs news">
  <div class="abs section-title" style="top:76px"><h2>LATEST NEWS</h2><span class="kicker">OUR BLOGS</span></div>

  <span class="abs slider-arrow" style="left:135px;background:#3a3a3a">
    <svg width="14" height="14" viewBox="0 0 20 20"><path d="M13 3l-7 7 7 7" fill="none" stroke="#fff" stroke-width="3"/></svg></span>
  <span class="abs slider-arrow" style="left:1024px;background:#dcdcdc">
    <svg width="14" height="14" viewBox="0 0 20 20"><path d="M7 3l7 7-7 7" fill="none" stroke="#fff" stroke-width="3"/></svg></span>

  <article class="abs news-card" style="left:212px">
    <div class="photo" role="img" aria-label="Photo of colleagues reviewing documents together" style="background:linear-gradient(135deg,#c9d4dc,#6f7d8a 50%,#1f2530)"></div>
    <span class="date"><svg width="11" height="11" viewBox="0 0 12 12"><rect x="1" y="2" width="10" height="9" fill="none" stroke="#c9a646"/><path d="M1 5h10" stroke="#c9a646"/></svg>April 5, 2025</span>
    <h3 class="hover">Sed ut perspiciatis unde omnis iste natus error sit voluptatem.</h3>
    <p>Lorem ipsum dolor sit amet, consectetur adipiscing elit, sed do eiusmod tempor incididunt ut labore et dolore magna aliqua. Ut enim ad minim veniam, quis nostrud exercitation ullamco laboris nisi ut aliquip ex ea commodo consequat.</p>
    <a class="pill read" href="#">Read More</a>
  </article>
  <article class="abs news-card" style="left:626px">
    <div class="photo" role="img" aria-label="Photo of a business team talking outside an office building" style="background:linear-gradient(135deg,#8a6a4e,#b8c2c8 45%,#2a2e36)"></div>
    <span class="date"><svg width="11" height="11" viewBox="0 0 12 12"><rect x="1" y="2" width="10" height="9" fill="none" stroke="#c9a646"/><path d="M1 5h10" stroke="#c9a646"/></svg>April 5, 2025</span>
    <h3>Sed ut perspiciatis unde omnis iste natus.</h3>
    <p>Lorem ipsum dolor sit amet, consectetur adipiscing elit, sed do eiusmod tempor incididunt ut labore et dolore magna aliqua. Ut enim ad minim veniam, quis nostrud exercitation ullamco laboris nisi ut aliquip ex ea commodo consequat.</p>
    <a class="pill read" href="#">Read More</a>
  </article>
</section>

<footer class="abs site-footer">
  <div class="abs brand"><span class="mark"></span>THORNFIELD MARSH, LLC</div>
  <div class="abs socials"><span></span><span></span><span></span></div>

  <div class="abs footer-col links">
    <h3>LINKS</h3>
    <ul><li>About Us</li><li>Services</li><li>Blogs</li><li>Contact Us</li></ul>
  </div>

  <div class="abs footer-col contact">
    <h3>CONTACT US</h3>
    <div class="contact-row" style="top:66px">
      <span class="ico"><svg width="14" height="16" viewBox="0 0 14 18"><path d="M7 1a6 6 0 0 0-6 6c0 4 6 10 6 10s6-6 6-10a6 6 0 0 0-6-6z" fill="#0a1f8f"/><circle cx="7" cy="7" r="2.2" fill="#fff"/></svg></span>
      <span>465, Lorem Ipsum<br>Lorem Ipsum , Lorem Ipsum</span>
    </div>
    <div class="contact-row" style="top:128px;align-items:center">
      <span class="ico"><svg width="14" height="14" viewBox="0 0 16 16"><path d="M3 1l3 3-2 2c1 2 3 4 5 5l2-2 3 3-2 3C7 15 1 9 1 3z" fill="#0a1f8f"/></svg></span>
      <span>+1 555 014 2287</span>
    </div>
    <div class="contact-row" style="top:171px;align-items:center">
      <span class="ico"><svg width="14" height="11" viewBox="0 0 16 12"><rect width="16" height="12" rx="1" fill="#0a1f8f"/><path d="M1 1l7 6 7-6" fill="none" stroke="#fff" stroke-width="1.4"/></svg></span>
      <span>hello@thornfieldmarsh.example</span>
    </div>
  </div>

  <div class="abs rule"></div>
  <p class="abs copyright">Copyright © 2025 All Rights Reserved By Thornfield Marsh, LLC</p>
</footer>

</body>
</html>
```